Business Card Design

We are a General Practice - Family medicine
We also have Allied Health professionals working within our team

Industry/Entity Type

Business

Contact Information for Business Card

Front of the card to display:

BRAMBLEWICK MEDICAL
PHONE 6348 2917

5/41 Fennimore Parade
Launceston Tasmania 7284

Back of the card to display:

My Appointments
Date:
Time:
With:

Please remember to phone us on 6348 2917 to cancel your appointment if you can't keep it.
A fee applied to missed appointments

```html
<!DOCTYPE html>
<html lang="en">
<head>
<meta charset="utf-8">
<title>Bramblewick Medical – Business Card</title>
<link rel="stylesheet" href="https://fonts.googleapis.com/css2?family=Open+Sans:wght@400;600&display=swap">
<style>
  :root {
    --sky: #3fa9de;
    --leaf: #8cc63f;
    --paper: #ffffff;
    --ink: #2b2b2b;
    --stage: #eceef0;
  }
  * { box-sizing: border-box; margin: 0; padding: 0; }
  html, body { width: 1200px; height: 900px; overflow: hidden; }
  body {
    background: var(--stage);
    font-family: "Open Sans", Arial, sans-serif;
    color: var(--ink);
    display: flex;
    flex-direction: column;
    align-items: center;
    justify-content: center;
    gap: 48px;
  }
  .card {
    position: relative;
    width: 640px;
    height: 366px;
    background: var(--paper);
    overflow: hidden;
    box-shadow: 0 6px 18px rgba(0,0,0,0.15);
  }
  .card-art { position: absolute; inset: 0; width: 100%; height: 100%; }
  .brand {
    position: absolute;
    display: flex;
    align-items: center;
    gap: 10px;
    font-size: 22px;
    font-weight: 400;
    color: var(--sky);
    white-space: nowrap;
  }
  .brand-dot {
    flex: none;
    width: 24px; height: 24px; border-radius: 50%;
    background: var(--leaf);
  }
  /* back */
  .card-back .brand { left: 200px; top: 72px; }
  .appointments {
    position: absolute; left: 70px; top: 170px;
    font-size: 15px; line-height: 19px;
  }
  .reminder {
    position: absolute; left: 70px; right: 40px; top: 262px;
    font-size: 9.5px; line-height: 13px; text-align: center;
  }
  /* front */
  .card-front .brand { right: 24px; top: 80px; }
  .practice-name {
    position: absolute; left: 200px; top: 200px;
    font-size: 21px; font-weight: 400; letter-spacing: 0.3px;
  }
  .contact-list { position: absolute; left: 200px; top: 246px; list-style: none; }
  .contact-item {
    display: flex; align-items: center; gap: 14px;
    font-size: 15px; line-height: 19px; margin-bottom: 12px;
  }
  .contact-icon {
    flex: none; width: 30px; height: 30px; border-radius: 50%;
    background: var(--sky);
    display: flex; align-items: center; justify-content: center;
  }
</style>
</head>
<body>

  <section class="card card-back" aria-label="Card back">
    <svg class="card-art" viewBox="0 0 640 366" aria-hidden="true">
      <path fill="var(--leaf)" d="M250 0 H640 V195 C590 95 450 22 250 0 Z"/>
      <path fill="var(--sky)" d="M340 0 H640 V125 C570 50 460 12 340 0 Z"/>
      <path fill="var(--sky)" d="M0 235 C70 305 190 345 320 366 H0 Z"/>
    </svg>
    <div class="brand"><span class="brand-dot"></span>Bramblewick Medical</div>
    <div class="appointments">
      <p>My Appointments</p>
      <p>Date:</p>
      <p>Time:</p>
      <p>With:</p>
    </div>
    <div class="reminder">
      <p>Please remember to phone us on 6348 2917 to cancel your appointment if you can't keep it.</p>
      <p>A fee applied to missed appointments</p>
    </div>
  </section>

  <section class="card card-front" aria-label="Card front">
    <svg class="card-art" viewBox="0 0 640 366" aria-hidden="true">
      <path fill="var(--leaf)" d="M0 0 H460 C330 70 200 200 150 366 H0 Z"/>
      <path fill="var(--sky)" d="M0 0 H420 C300 60 160 200 110 366 H0 Z"/>
      <path fill="var(--sky)" d="M640 185 C605 275 530 330 455 366 H640 Z"/>
    </svg>
    <div class="brand"><span class="brand-dot"></span>Bramblewick Medical</div>
    <h1 class="practice-name">BRAMBLEWICK MEDICAL</h1>
    <ul class="contact-list">
      <li class="contact-item">
        <span class="contact-icon">
          <svg width="16" height="16" viewBox="0 0 24 24" aria-hidden="true"><path fill="#fff" d="M6.6 10.8a15.1 15.1 0 0 0 6.6 6.6l2.2-2.2c.3-.3.7-.4 1-.2 1.1.4 2.3.6 3.600.6.6 0 1 .4 1 1V20c0 .6-.4 1-1 1A17 17 0 0 1 3 4c0-.6.4-1 1-1h3.5c.6 0 1 .4 1 1 0 1.3.2 2.5.6 3.6.1.3 0 .7-.2 1z"/></svg>
        </span>
        <span>6348 2917</span>
      </li>
      <li class="contact-item">
        <span class="contact-icon">
          <svg width="14" height="16" viewBox="0 0 24 24" aria-hidden="true"><path fill="#fff" d="M12 2a7 7 0 0 0-7 7c0 5.2 7 13 7 13s7-7.8 7-13a7 7 0 0 0-7-7zm0 9.5A2.5 2.5 0 1 1 12 6.5a2.5 2.5 0 0 1 0 5z"/></svg>
        </span>
        <span>5/41 Fennimore Parade<br>Launceston Tasmania 7284</span>
      </li>
    </ul>
  </section>

</body>
</html>
```